pvt business card

need clean and modern business card design, possibly two. Logo on front and writing on back-Full source files for logo attached-THE CHOSEN LOGO IS SQUARE PVT with PVT HOLDINGS in ALL BLUE. Please do not use any other logos from files, this is source file that includes correct logo

```html
<!DOCTYPE html>
<html lang="en">
<head>
<meta charset="utf-8">
<title>PVT Holdings Business Card</title>
<link href="https://fonts.googleapis.com/css2?family=Open+Sans:wght@400;600;700&display=swap" rel="stylesheet">
<style>
  :root {
    --page-bg: #eeeeee;
    --brand-blue: #3779bf;
    --brand-deep: #1f4f9a;
    --card-white: #f8f8f8;
    --ink: #2b2b2b;
    --rule: #8a8a8a;
  }
  * { margin: 0; padding: 0; box-sizing: border-box; }
  html, body {
    width: 1200px; height: 1200px; overflow: hidden;
    background: var(--page-bg);
    font-family: "Open Sans", Arial, sans-serif;
  }
  .canvas {
    position: relative; width: 1200px; height: 1200px;
    display: flex; flex-direction: column; align-items: center; justify-content: center; gap: 60px;
  }
  .card {
    width: 770px; height: 440px; position: relative;
    box-shadow: 0 6px 18px rgba(0,0,0,0.12);
  }
  .card-front {
    background: var(--brand-blue);
    display: flex; align-items: center; justify-content: center;
  }
  .front-mark {
    display: flex; align-items: center; gap: 18px;
    color: var(--brand-deep);
    font-weight: 700; font-size: 64px; letter-spacing: 6px;
  }
  .mark-square {
    width: 44px; height: 44px; background: var(--brand-deep);
  }
  .card-back {
    background: var(--card-white);
    display: flex; align-items: center;
  }
  .back-brand {
    width: 52%; display: flex; align-items: center; justify-content: center;
    gap: 14px; color: var(--brand-blue);
    font-weight: 600; font-size: 36px; letter-spacing: 3px;
  }
  .back-brand .mark-square { width: 30px; height: 30px; background: var(--brand-blue); }
  .divider {
    width: 1px; height: 250px; background: var(--rule);
  }
  .contact {
    padding-left: 44px; color: var(--ink); font-size: 19px; line-height: 1.32;
  }
  .contact-name { color: var(--brand-blue); font-weight: 700; font-size: 25px; line-height: 1.2; }
  .contact-title { margin-bottom: 30px; }
  .contact-line { display: flex; align-items: center; gap: 10px; }
  .contact-line svg { width: 16px; height: 16px; flex: none; }
</style>
</head>
<body>
<main class="canvas">
  <section class="card card-front" aria-label="Card front">
    <div class="front-mark"><span class="mark-square"></span>PVT</div>
  </section>

  <section class="card card-back" aria-label="Card back">
    <div class="back-brand"><span class="mark-square"></span>PVT HOLDINGS</div>
    <div class="divider"></div>
    <div class="contact">
      <p class="contact-name">Daniel Reyes</p>
      <p class="contact-title">President</p>
      <p>480 Harbor Lane, Suite 12</p>
      <p>Coral Bay, Florida, 33001</p>
      <p class="contact-line">
        <svg viewBox="0 0 16 16" aria-hidden="true"><path d="M4 1.5 6.5 4 5 6c.9 2 2.6 3.8 5 5l2-1.5 2.5 2.5-1.8 2.2C7.5 14 2 8.5 1.8 3.3z" fill="#3779bf"/></svg>
        (555) 210-7784
      </p>
      <p class="contact-line">
        <svg viewBox="0 0 16 16" aria-hidden="true"><rect x="1" y="3" width="14" height="10" fill="none" stroke="#3779bf" stroke-width="1.6"/><path d="M1.5 3.5 8 9l6.5-5.5" fill="none" stroke="#3779bf" stroke-width="1.6"/></svg>
        daniel@pvtholdings.com
      </p>
      <p class="contact-line">
        <svg viewBox="0 0 16 16" aria-hidden="true"><circle cx="8" cy="8" r="6.5" fill="none" stroke="#3779bf" stroke-width="1.5"/><ellipse cx="8" cy="8" rx="3" ry="6.5" fill="none" stroke="#3779bf" stroke-width="1.2"/><path d="M1.5 8h13M2.5 5h11M2.5 11h11" stroke="#3779bf" stroke-width="1.1"/></svg>
        www.pvtholdings.com
      </p>
    </div>
  </section>
</main>
</body>
</html>
```